Dental Practice Billboard Design

We are a newer dental practice in need of a simple but appealing billboard for our growing dental practice to attract new patients. The practice is owned by husband and wife dentists and is family friendly in a small town in Kentucky. We try to be very friendly and caring to our patients. Would prefer a blue background for the billboard and our tooth logo to be prominent. We are partial to the Patua One font used in the image below but please feel free to tweak it as you deem necessary. The shape of the uppercase D and lowercase g are why we like that font, so fonts with a similarly shaped “D” and “g” would work as well. Please include our phone number (606) 847-3190. Please see our website Halvorcrestdentistry.com for more info on the practice if needed. Thank you! Looking forward to seeing your creation.
Updates

The dimensions will be 12ft x 24ft (3.6576m x 7.3152m). Apologies for not including this in the original prompt. Thank you all for your submissions.

Industry/Entity Type

Dental

Font styles to use
Other font styles liked:
• Patua One

Colors
0054AA
0677BA
7BADD7
CADEEF
E8F1F8
0094D4
00A9DD
6FCCEA
C7EBF8
E9F6FB
00AB8E
00BBA5
67D7C9
C6EFE9
E9F9F6
59FF00
82FF00
B8FF75
E3FFCB
F4FFEA

Requirements
Must have
• Phone number, website, Logo, Practice name “Halvor Crest Dentistry”
Should not have
• A tagline or slogan

```html
<!DOCTYPE html>
<html lang="en">
<head>
<meta charset="utf-8">
<title>Halvor Crest Dentistry Billboard</title>
<link rel="stylesheet" href="https://fonts.googleapis.com/css2?family=Patua+One&family=Fira+Sans:wght@600&display=swap">
<style>
  :root {
    --navy: #1f4a86;
    --brand-blue: #3c5d9c;
    --sky-light: #e8f1f8;
    --sky-mid: #cadeef;
    --green: #2fa84a;
    --green-light: #6abd45;
    --white: #ffffff;
    --page-bg: #eef2f6;
    --photo-warm: #d9c3b4;
    --photo-coat: #f1f1f1;
  }
  * { margin: 0; padding: 0; box-sizing: border-box; }
  html, body { width: 1200px; height: 900px; overflow: hidden; }
  body {
    background: var(--page-bg);
    display: flex;
    align-items: center;
    justify-content: center;
  }
  .billboard {
    position: relative;
    width: 1200px;
    height: 600px;
    overflow: hidden;
    background: radial-gradient(ellipse at 62% 38%, var(--white) 0%, var(--sky-light) 35%, var(--sky-mid) 100%);
  }
  .photo-panel {
    position: absolute;
    left: 0; top: 0;
    width: 470px; height: 600px;
  }
  .photo-panel svg { width: 100%; height: 100%; display: block; }
  .brand {
    position: absolute;
    left: 470px; top: 60px;
    display: flex;
    align-items: center;
    gap: 30px;
  }
  .brand-dot {
    width: 150px; height: 150px;
    border-radius: 50%;
    background: var(--brand-blue);
    flex: none;
  }
  .brand-name {
    font-family: "Patua One", Georgia, serif;
    color: var(--brand-blue);
    line-height: 0.95;
  }
  .brand-name .primary { display: block; font-size: 138px; }
  .brand-name .secondary { display: block; font-size: 62px; margin-left: 4px; }
  .phone-band {
    position: absolute;
    left: 470px; top: 350px;
    width: 730px; height: 108px;
    display: flex;
  }
  .phone-icon {
    width: 100px; height: 108px;
    background: linear-gradient(180deg, var(--green) 0%, var(--green-light) 100%);
    border-radius: 18px 0 0 18px;
    display: flex; align-items: center; justify-content: center;
    flex: none;
  }
  .phone-number {
    flex: 1;
    background: var(--navy);
    border-radius: 30px 0 0 30px;
    margin-left: -14px;
    color: var(--white);
    font-family: "Fira Sans", Arial, sans-serif;
    font-weight: 600;
    font-size: 84px;
    display: flex; align-items: center;
    padding-left: 42px;
    letter-spacing: 1px;
  }
  .website {
    position: absolute;
    left: 480px; top: 492px;
    display: flex; align-items: center; gap: 22px;
    font-family: "Patua One", Georgia, serif;
    font-size: 46px;
    color: var(--navy);
  }
</style>
</head>
<body>
  <main class="billboard">
    <div class="photo-panel">
      <svg viewBox="0 0 470 600" aria-hidden="false">
        <defs>
          <linearGradient id="photoTone" x1="0" y1="0" x2="0" y2="1">
            <stop offset="0" stop-color="var(--photo-warm)"/>
            <stop offset="1" stop-color="var(--photo-coat)"/>
          </linearGradient>
        </defs>
        <path d="M0 0 H400 C470 180 440 430 330 600 H0 Z" fill="var(--white)"/>
        <rect x="40" y="70" width="340" height="490" rx="150" fill="url(#photoTone)"
              role="img" aria-label="Photo of the two smiling dentists in white coats"/>
      </svg>
    </div>

    <div class="brand">
      <span class="brand-dot" aria-hidden="true"></span>
      <h1 class="brand-name">
        <span class="primary">Halvor</span>
        <span class="secondary">Crest Dentistry</span>
      </h1>
    </div>

    <div class="phone-band">
      <div class="phone-icon">
        <svg width="54" height="54" viewBox="0 0 24 24" aria-hidden="true">
          <path fill="#ffffff" d="M6.6 10.8a15.1 15.1 0 0 0 6.6 6.6l2.2-2.2a1 1 0 0 1 1-.25 11.4 11.4 0 0 0 3.6.57 1 1 0 0 1 1 1V20a1 1 0 0 1-1 1A17 17 0 0 1 3 4a1 1 0 0 1 1-1h3.5a1 1 0 0 1 1 1c0 1.25.2 2.45.57 3.6a1 1 0 0 1-.25 1z"/>
        </svg>
      </div>
      <div class="phone-number">(606) 847-3190</div>
    </div>

    <div class="website">
      <svg width="34" height="34" viewBox="0 0 24 24" aria-hidden="true">
        <path fill="var(--navy)" d="M3 3 L20 9 L13 12 L21 20 L19 22 L11 14 L8 21 Z"/>
      </svg>
      <span>www.halvorcrestdentistry.com</span>
    </div>
  </main>
</body>
</html>
```